Maple Syrup Bottle (front) Label design

I need label design for a 16fl OZ rectangular bottle of maple syrup with the usable dimensions of: Front: 4" x 2" and the back area for "ingredient specifications" of: 6" x 2". The maple syrup product comes from our own farm and is a quality product. The technical name/class of the syrup is: Grade A / AMBER
Updates

I can’t seem to find a way to upload a photo of the maple syrup bottle, but the front dimensions are clearly written on bottle description. Again: 4.5” by 2.25”

I have tried to upload the photo of the maple syrup bottle several times, and it seems (from my side) that it is successful. But I can never find it and the artists cannot find it either. Not sure what to do.

I have tried several times to add a photo of maple bottle, but it never shows up

This seems to be a futile exercise

I would like to post some images of the actual cedar Hollow (not the one on Quorvo, though!
But I can’t get back to the page that allows that to happen. Please advise!

Somebody PLEASE ask PV management to make it possible for me to upload more images! The "add photos" etc. just disappears from anywhere.

Target Market(s)

High-end food stores

Industry/Entity Type

Maple syrup retail industry

Font styles to use
Other font styles liked:
• I don't know, and welcome suggestions

Colors

Designer to choose colors to be used in the design.

Requirements
Must have
• Name of Farm: Cedar Hollow Maple
Nice to have
• The label can be "minimalist" and elegant. There is already a Maple leaf glass relief on the top of front of the bottle.
Should not have
• and NOT include farm buildings with steam coming out the chimney, etc.

```html
<!DOCTYPE html>
<html lang="en">
<head>
<meta charset="utf-8">
<title>Cedar Hollow Maple – Maple Syrup Front Label</title>
<link rel="stylesheet" href="https://fonts.googleapis.com/css2?family=Cabin:wght@400;500&family=Cinzel:wght@900&family=Quicksand:wght@600&display=swap">
<style>
  :root {
    --backdrop: #2f2f2f;
    --label-top: #e4e3e1;
    --label-mid: #ffffff;
    --label-low: #f2f7fb;
    --label-bottom: #e3ddd4;
    --rim-light: #fafafa;
    --rim-dark: #9e9e9e;
    --ink: #111111;
    --forest: #2c4a12;
    --grade-red: #b3261e;
    --mist-dark: #6e6e6e;
    --mist-light: #c9c9c9;
    --gold-light: #f1e2b8;
    --gold-deep: #b8955a;
  }
  * { margin: 0; padding: 0; box-sizing: border-box; }
  html, body { width: 901px; height: 1200px; overflow: hidden; background: var(--backdrop); }
  .canvas { position: relative; width: 901px; height: 1200px; }

  .label { position: absolute; left: 170px; top: 69px; width: 560px; height: 1062px; }
  .label-frame { position: absolute; inset: 0; }

  .landscape-art {
    position: absolute; left: 34px; top: 165px; width: 492px; height: 185px;
    background: linear-gradient(180deg, var(--mist-light) 0%, #a9a9a9 45%, var(--mist-dark) 70%, rgba(255,255,255,0) 100%);
    border-radius: 60px 60px 0 0;
  }

  .product-name {
    position: absolute; top: 395px; left: 0; width: 560px; text-align: center;
    font-family: "Cinzel", serif; font-weight: 900; font-size: 50px;
    letter-spacing: 3px; color: var(--forest);
  }
  .product-grade {
    position: absolute; top: 466px; left: 0; width: 560px; text-align: center;
    font-family: "Cabin", sans-serif; font-weight: 400; font-size: 34px; color: var(--grade-red);
  }
  .leaves-art {
    position: absolute; left: 120px; top: 545px; width: 330px; height: 380px;
    background: radial-gradient(ellipse at 50% 45%, var(--gold-deep) 0%, var(--gold-light) 55%, rgba(255,255,255,0) 75%);
  }
  .volume {
    position: absolute; top: 960px; left: 0; width: 560px; text-align: center;
    font-family: "Quicksand", sans-serif; font-weight: 600; font-size: 34px; color: var(--ink);
  }
</style>
</head>
<body>
<main class="canvas">
  <section class="label">
    <svg class="label-frame" width="560" height="1062" viewBox="0 0 560 1062">
      <defs>
        <linearGradient id="label-fill" x1="0" y1="0" x2="0" y2="1">
          <stop offset="0" stop-color="var(--label-top)"/>
          <stop offset="0.45" stop-color="var(--label-mid)"/>
          <stop offset="0.8" stop-color="var(--label-low)"/>
          <stop offset="1" stop-color="var(--label-bottom)"/>
        </linearGradient>
        <linearGradient id="rim" x1="0" y1="0" x2="1" y2="1">
          <stop offset="0" stop-color="var(--rim-light)"/>
          <stop offset="0.5" stop-color="var(--rim-dark)"/>
          <stop offset="1" stop-color="var(--rim-light)"/>
        </linearGradient>
        <path id="farm-arc" d="M 80,190 A 240 240 0 0 1 480,190"/>
      </defs>
      <rect x="3" y="3" width="554" height="1056" rx="277" fill="url(#rim)"/>
      <rect x="12" y="12" width="536" height="1038" rx="268" fill="url(#label-fill)" stroke="var(--rim-dark)" stroke-width="2"/>
      <text font-family="Quicksand, sans-serif" font-weight="600" font-size="32" fill="var(--ink)" letter-spacing="1">
        <textPath href="#farm-arc" startOffset="50%" text-anchor="middle">Cedar Hollow Maple</textPath>
      </text>
    </svg>

    <div class="landscape-art" role="img" aria-label="Misty mountain ridge with a line of bare trees"></div>

    <h1 class="product-name">MAPLE SYRUP</h1>
    <p class="product-grade">Grade A /Amber</p>

    <div class="leaves-art" role="img" aria-label="Gold foil maple leaves on a branch"></div>

    <p class="volume">180ml</p>
  </section>
</main>
</body>
</html>
```